Holbys Pet Care

Hi. I need a business card /logo for my pet care business. Im thinking about a dogs paw print. Although i do look after other pets so don't want to restrict my self. Open to suggestions on colour etc but like greens and purples.The name of my business is holby's pet care. The logo could be just an image or have holbys power care on it. An option to do either would be great. For the winner i also would like a Web page (word press template if possible) designed if you can, of course I'll pay additional for this. Look forward to your ideas!

```html
<!DOCTYPE html>
<html lang="en">
<head>
<meta charset="utf-8">
<title>Holby's Pet Care – Business Card</title>
<link rel="stylesheet" href="https://fonts.googleapis.com/css2?family=Federo&family=Mulish:wght@400&display=swap">
<style>
  :root {
    --backdrop: #e6e0d6;
    --card-light: #6a9a5c;
    --card-mid: #4f8044;
    --card-dark: #3c6636;
    --ink: #f4f7f1;
    --ink-soft: rgba(244, 247, 241, 0.88);
    --frost: rgba(235, 240, 232, 0.55);
  }
  * { margin: 0; padding: 0; box-sizing: border-box; }
  html, body {
    width: 1200px;
    height: 970px;
    overflow: hidden;
    background: var(--backdrop);
  }
  .card {
    position: absolute;
    left: 100px;
    top: 207px;
    width: 1000px;
    height: 556px;
    border-radius: 4px;
    background: linear-gradient(160deg, var(--card-light) 0%, var(--card-mid) 45%, var(--card-dark) 100%);
    box-shadow: 0 12px 30px rgba(0, 0, 0, 0.18);
  }
  .brand-name {
    position: absolute;
    right: 552px;
    top: 112px;
    text-align: right;
    font-family: "Federo", sans-serif;
    color: var(--ink);
    text-transform: uppercase;
    line-height: 1;
  }
  .brand-name .line-1 { display: block; font-size: 58px; letter-spacing: 1px; }
  .brand-name .line-2 { display: block; font-size: 44px; margin-top: 18px; letter-spacing: 1px; }
  .contacts {
    position: absolute;
    right: 552px;
    top: 290px;
    list-style: none;
    font-family: "Mulish", sans-serif;
    font-size: 18px;
    color: var(--ink-soft);
  }
  .contacts li {
    display: flex;
    align-items: center;
    justify-content: flex-end;
    height: 38px;
  }
  .contacts .icon {
    width: 22px;
    height: 22px;
    margin-left: 14px;
    flex: none;
  }
  .mark {
    position: absolute;
    left: 477px;
    top: 123px;
    width: 249px;
    height: 308px;
    border-radius: 14px;
    background: var(--frost);
  }
  .mark-name {
    position: absolute;
    left: 752px;
    top: 250px;
    font-family: "Federo", sans-serif;
    font-size: 46px;
    color: var(--ink);
    text-transform: uppercase;
    letter-spacing: 1px;
  }
</style>
</head>
<body>
  <div class="card">
    <h1 class="brand-name">
      <span class="line-1">Holby's</span>
      <span class="line-2">Pet Care</span>
    </h1>

    <ul class="contacts">
      <li>555.555.0147
        <svg class="icon" viewBox="0 0 24 24" aria-hidden="true">
          <path d="M8 3c-2 1-3 3-3 6 0 6 4 11 9 12 2 0 3-1 4-2l-3-4-2 1c-2-1-3-4-3-6l2-1-2-5z" fill="none" stroke="#f4f7f1" stroke-width="1.8" stroke-linejoin="round"/>
        </svg>
      </li>
      <li>social.co.uk/holbys
        <svg class="icon" viewBox="0 0 24 24" aria-hidden="true">
          <circle cx="12" cy="12" r="8" fill="#f4f7f1"/>
        </svg>
      </li>
      <li>hello@holbyspetcare.co.uk
        <svg class="icon" viewBox="0 0 24 24" aria-hidden="true">
          <rect x="2" y="5" width="20" height="14" fill="none" stroke="#f4f7f1" stroke-width="1.8"/>
          <path d="M2 5l10 8 10-8M2 19l7-7M22 19l-7-7" fill="none" stroke="#f4f7f1" stroke-width="1.6"/>
        </svg>
      </li>
      <li>holbyspetcare.co.uk
        <svg class="icon" viewBox="0 0 24 24" aria-hidden="true">
          <circle cx="12" cy="12" r="9" fill="none" stroke="#f4f7f1" stroke-width="1.6"/>
          <ellipse cx="12" cy="12" rx="4" ry="9" fill="none" stroke="#f4f7f1" stroke-width="1.4"/>
          <path d="M3 12h18M5 7h14M5 17h14" fill="none" stroke="#f4f7f1" stroke-width="1.3"/>
        </svg>
      </li>
    </ul>

    <div class="mark" aria-hidden="true"></div>
    <span class="mark-name">Holby's</span>
  </div>
</body>
</html>
```